Business Card Design for Varnor Facility Services

We are looking for a Business Card Design for the Company "Varnor Facility Services."
Front side:
- Company Logo (small)
- Company Name, address, pohone, website and personal data.
- white background, for text e.g. company colors (blue or green like in the logo)
Please use following data:
Company data:
Varnor Facility Services Kuttelbrand
Lindauweg 14
4817 Brannwil
www.varnor-fs.example
Person data:
Tobias Kuttelbrand
Geschäftsführer
+41 76 915 47 18
info@varnor-fs.example
Back side:
could be colored in blue or green
please use a big logo sing and some smaller icons to say what is all beeing offered in facility services, like cleaning, maintenance cleaning
industrial cleaning, caretaking, gardening, disposal. There is no need for everyone of the icons if there are similar or an icon is standing for more of them.
Cleaning Service
colors to use:
blue: HEX 246BB0
green: HEX 52B33E

```html
<!DOCTYPE html>
<html lang="de">
<head>
<meta charset="utf-8">
<title>Varnor Facility Services – Business Card</title>
<link rel="stylesheet" href="https://fonts.googleapis.com/css2?family=Open+Sans:wght@400;600;700&display=swap">
<style>
  :root {
    --brand-blue: #246bb0;
    --brand-green: #52b33e;
    --paper: #ffffff;
    --ink: #3a3a3a;
    --rule: #8a8a8a;
    --stage: #2b2b2b;
    --icon-tint: #5e94c9;
  }
  * { box-sizing: border-box; margin: 0; padding: 0; }
  html, body { width: 1200px; height: 895px; overflow: hidden; }
  body {
    background: var(--stage);
    font-family: "Open Sans", Arial, sans-serif;
    display: flex; flex-direction: column; align-items: center;
    justify-content: center; gap: 25px;
  }
  .card {
    width: 618px; height: 400px; position: relative;
    box-shadow: 0 10px 30px rgba(0,0,0,.45);
  }

  /* Back side */
  .card--back { background: var(--brand-blue); color: var(--paper); }
  .back-brand {
    position: absolute; top: 88px; left: 0; right: 0; text-align: center;
  }
  .back-brand__mark {
    display: inline-block; width: 26px; height: 26px; border-radius: 50%;
    background: var(--paper); vertical-align: middle; margin-right: 14px;
  }
  .back-brand__name {
    font-size: 50px; font-weight: 700; letter-spacing: 3px;
    vertical-align: middle; color: var(--paper);
  }
  .back-brand__tag {
    display: block; margin-top: 4px; font-size: 20px; font-weight: 700;
    letter-spacing: 5px; color: var(--paper);
  }
  .services {
    position: absolute; left: 24px; right: 24px; bottom: 46px;
    display: flex; justify-content: space-between; list-style: none;
  }
  .service { display: flex; flex-direction: column; align-items: center; gap: 10px; width: 112px; }
  .service__icon { width: 40px; height: 40px; border-radius: 8px; background: var(--icon-tint); }
  .service__label { font-size: 13px; letter-spacing: .4px; white-space: nowrap; }

  /* Front side */
  .card--front { background: var(--paper); color: var(--ink); }
  .front-brand { position: absolute; top: 70px; right: 60px; text-align: right; }
  .front-brand__mark {
    display: inline-block; width: 22px; height: 22px; border-radius: 50%;
    background: var(--brand-blue); vertical-align: middle; margin-right: 12px;
  }
  .front-brand__name {
    font-size: 44px; font-weight: 700; letter-spacing: 3px;
    color: var(--brand-blue); vertical-align: middle;
  }
  .front-brand__tag {
    display: block; font-size: 17px; font-weight: 700; letter-spacing: 4px;
    color: var(--brand-blue);
  }
  .details { position: absolute; left: 20px; right: 20px; top: 222px; display: flex; }
  .person { width: 290px; text-align: right; padding-right: 18px; }
  .divider { width: 1px; background: var(--rule); height: 120px; }
  .company { padding-left: 18px; }
  .person__name {
    font-size: 20px; font-weight: 600; color: var(--brand-blue);
    text-transform: uppercase; letter-spacing: .5px; white-space: nowrap;
  }
  .person__role { font-size: 14px; margin-bottom: 8px; }
  .line { font-size: 15px; line-height: 25px; display: flex; align-items: center; gap: 8px; white-space: nowrap; }
  .person .line { justify-content: flex-end; }
  .line svg { width: 16px; height: 16px; flex: none; }
  .company__name { font-size: 14px; font-weight: 600; color: var(--brand-blue); line-height: 25px; white-space: nowrap; }
</style>
</head>
<body>

<section class="card card--back" aria-label="Back side">
  <div class="back-brand">
    <span class="back-brand__mark"></span><span class="back-brand__name">VARNOR</span>
    <span class="back-brand__tag">FACILITY SERVICES</span>
  </div>
  <ul class="services">
    <li class="service"><span class="service__icon" role="img" aria-label="Icon of a cleaner with mop and bucket"></span><span class="service__label">Cleaning</span></li>
    <li class="service"><span class="service__icon" role="img" aria-label="Icon of a waste bin"></span><span class="service__label">Disposal</span></li>
    <li class="service"><span class="service__icon" role="img" aria-label="Icon of a factory building"></span><span class="service__label">Industrial Cleaning</span></li>
    <li class="service"><span class="service__icon" role="img" aria-label="Icon of a hand holding a seedling"></span><span class="service__label">Gardening</span></li>
    <li class="service"><span class="service__icon" role="img" aria-label="Icon of a caretaker"></span><span class="service__label">Caretaking</span></li>
  </ul>
</section>

<section class="card card--front" aria-label="Front side">
  <div class="front-brand">
    <span class="front-brand__mark"></span><span class="front-brand__name">VARNOR</span>
    <span class="front-brand__tag">FACILITY SERVICES</span>
  </div>
  <div class="details">
    <div class="person">
      <p class="person__name">Tobias Kuttelbrand</p>
      <p class="person__role">Geschäftsführer</p>
      <p class="line">+41 76 915 47 18
        <svg viewBox="0 0 16 16" aria-hidden="true"><circle cx="8" cy="8" r="8" fill="var(--brand-green)"/><path d="M5.2 4.2l1.5-.4.8 1.9-1 .7a5 5 0 0 0 2.2 2.2l.7-1 1.9.8-.4 1.5c-3.4.2-5.9-2.3-5.7-5.7z" fill="#fff"/></svg></p>
      <p class="line">info@varnor-fs.example
        <svg viewBox="0 0 16 16" aria-hidden="true"><circle cx="8" cy="8" r="8" fill="var(--brand-green)"/><rect x="4" y="5" width="8" height="6" rx="1" fill="#fff"/><path d="M4.3 5.4L8 8.3l3.7-2.9" stroke="var(--brand-green)" fill="none"/></svg></p>
    </div>
    <div class="divider"></div>
    <div class="company">
      <p class="company__name">Varnor Facility Services Kuttelbrand</p>
      <p class="line">Lindauweg 14</p>
      <p class="line">4817 Brannwil</p>
      <p class="line">
        <svg viewBox="0 0 16 16" aria-hidden="true"><circle cx="8" cy="8" r="8" fill="var(--brand-green)"/><circle cx="8" cy="8" r="4.2" fill="none" stroke="#fff"/><ellipse cx="8" cy="8" rx="1.8" ry="4.2" fill="none" stroke="#fff"/><path d="M3.8 8h8.4" stroke="#fff"/></svg>
        www.varnor-fs.example</p>
    </div>
  </div>
</section>

</body>
</html>
```